Toravel Project Consulting

I need a logo and business card design for a small business operating in the management consulting and contractor space, predominantly in local and state government. I specialise in project management, financial consulting, people and culture, procurement, ICT transformation and contracting for corporate support areas of organisations.

Industry/Entity Type

Business

```html
<!DOCTYPE html>
<html lang="en">
<head>
<meta charset="utf-8">
<title>Toravel Project Consulting – Business Card</title>
<link rel="stylesheet" href="https://fonts.googleapis.com/css2?family=Oswald:wght@400;500&display=swap">
<style>
  :root {
    --band-deep: #2b2c86;
    --band-mid: #1a6fc2;
    --band-bright: #2ea8e2;
    --card-white: #ffffff;
    --ink-light: #ffffff;
    --ink-grey: #6a6a6a;
  }
  html, body {
    margin: 0;
    padding: 0;
    overflow: hidden;
    background: var(--card-white);
  }
  .card {
    position: relative;
    width: 1200px;
    height: 669px;
    overflow: hidden;
    background: var(--card-white);
    font-family: "Oswald", sans-serif;
    text-transform: uppercase;
  }
  .brand-band {
    position: absolute;
    left: 0;
    top: 0;
    width: 1200px;
    height: 435px;
    background:
      radial-gradient(ellipse 520px 300px at 120px 90px, rgba(43,44,134,0.95), rgba(43,44,134,0) 100%),
      radial-gradient(ellipse 380px 220px at 1000px 330px, var(--band-bright), rgba(46,168,226,0) 100%),
      linear-gradient(180deg, #1b68bd 0%, var(--band-mid) 60%, #1f80cc 100%);
  }
  .wordmark {
    position: absolute;
    left: 686px;
    top: 96px;
    color: var(--ink-light);
    font-weight: 500;
    display: flex;
    align-items: center;
    gap: 20px;
  }
  .wordmark-square {
    width: 62px;
    height: 62px;
    background: var(--ink-light);
    flex: none;
  }
  .wordmark-name {
    line-height: 1;
  }
  .wordmark-name .primary {
    display: block;
    font-size: 74px;
    letter-spacing: 2px;
  }
  .wordmark-name .secondary {
    display: block;
    font-size: 30px;
    letter-spacing: 5px;
    margin-top: 8px;
  }
  .person {
    position: absolute;
    left: 680px;
    top: 296px;
    color: var(--ink-light);
    font-weight: 500;
    line-height: 1;
  }
  .person-name {
    font-size: 50px;
    letter-spacing: 2px;
    margin: 0;
  }
  .person-role {
    font-size: 30px;
    letter-spacing: 2px;
    margin: 8px 0 0;
  }
  .contact {
    position: absolute;
    left: 680px;
    top: 452px;
    margin: 0;
    padding: 0;
    list-style: none;
    color: var(--ink-grey);
    font-weight: 500;
    font-size: 34px;
    letter-spacing: 2.5px;
    line-height: 41px;
  }
</style>
</head>
<body>
  <div class="card">
    <div class="brand-band"></div>

    <div class="wordmark">
      <span class="wordmark-square"></span>
      <span class="wordmark-name">
        <span class="primary">Toravel</span>
        <span class="secondary">Project Consulting</span>
      </span>
    </div>

    <div class="person">
      <p class="person-name">Evan Marsh</p>
      <p class="person-role">Director</p>
    </div>

    <ul class="contact">
      <li>14 Halden Parade</li>
      <li>Larkfield NSW 2063</li>
      <li>Fon: 555-810-442</li>
      <li>Mail: toravelpc@mailbox.com</li>
    </ul>
  </div>
</body>
</html>
```